Modern business card design for professional copywriter

I'd like a business card design that I can use to have my cards printed out by plink.com as a squared corners business card (see artwork and design guidelines here: https://help.plink.com/hc/en-gb/sections/300481726-PLINK-Product-Templates)

The design should be clean and modern and reflect the colours, tone and branding on my website: https://noravestrel.com.au

Target Market(s)

Professionals, B2B small business owners

Industry/Entity Type

Business

Contact Information for Business Card

Nora Vestrel
m: 0427 593 864
e: nora@noravestrel.com.au
w: noravestrel.com.au

Font styles to use
Sans Serif

Requirements
Must have
• Tagline: "Smart copywriting for clever business people"
• Brand colours: fd8000, 009984, 666666 and black
Nice to have

```html
<!DOCTYPE html>
<html lang="en">
<head>
<meta charset="utf-8">
<title>Nora Vestrel – Business Card</title>
<link rel="stylesheet" href="https://fonts.googleapis.com/css2?family=Jost:wght@300;400;500&display=swap">
<style>
  :root {
    --teal: #009984;
    --orange: #fd8000;
    --grey: #666666;
    --ink: #000000;
    --paper: #ffffff;
    --backdrop: #ecebe8;
    --photo-light: #f4f1ec;
    --photo-mid: #e3d6c2;
  }
  * { box-sizing: border-box; margin: 0; padding: 0; }
  html, body {
    width: 1200px;
    height: 1000px;
    overflow: hidden;
    background: var(--backdrop);
    font-family: "Jost", Arial, sans-serif;
  }
  .canvas {
    position: relative;
    width: 1200px;
    height: 1000px;
  }
  .card {
    position: absolute;
    left: 290px;
    width: 620px;
    height: 355px;
    background: var(--paper);
    overflow: hidden;
    box-shadow: 0 6px 18px rgba(0,0,0,0.12);
  }
  .card--front { top: 120px; }
  .card--back  { top: 525px; }

  /* Front */
  .tagline-band {
    position: absolute;
    left: 0; top: 0;
    width: 100%;
    height: 40px;
    background: var(--teal);
    color: var(--paper);
    font-weight: 300;
    font-size: 19px;
    letter-spacing: 2.4px;
    line-height: 40px;
    padding-left: 58px;
  }
  .front-name {
    position: absolute;
    left: 66px;
    top: 92px;
    font-size: 50px;
    font-weight: 400;
    color: var(--teal);
    letter-spacing: -0.5px;
  }
  .portrait {
    position: absolute;
    right: 0;
    top: 40px;
    width: 210px;
    height: 315px;
    background: linear-gradient(160deg, var(--photo-mid) 0%, var(--photo-light) 55%, var(--paper) 100%);
  }
  .contact-list {
    position: absolute;
    left: 66px;
    bottom: 36px;
    list-style: none;
    color: var(--grey);
    font-size: 22px;
    font-weight: 300;
    line-height: 38px;
  }
  .contact-list .label {
    color: var(--teal);
    font-weight: 500;
    margin-right: 8px;
  }

  /* Back */
  .back-band-top {
    position: absolute;
    left: 0; top: 0;
    width: 100%;
    height: 42px;
    background: var(--teal);
    color: var(--paper);
    font-weight: 300;
    font-size: 19px;
    letter-spacing: 2.4px;
    line-height: 42px;
    padding-left: 270px;
  }
  .back-band-bottom {
    position: absolute;
    left: 0; bottom: 0;
    width: 100%;
    height: 64px;
    background: var(--teal);
    color: var(--paper);
    font-weight: 300;
    font-size: 19px;
    letter-spacing: 2.4px;
    line-height: 64px;
    text-align: center;
  }
  .brand {
    position: absolute;
    left: 0;
    top: 42px;
    width: 100%;
    height: 249px;
    display: flex;
    align-items: center;
    justify-content: center;
    gap: 18px;
  }
  .brand-mark {
    width: 22px;
    height: 22px;
    background: var(--orange);
  }
  .brand-name {
    font-size: 58px;
    font-weight: 400;
    color: var(--teal);
    letter-spacing: -0.5px;
  }
</style>
</head>
<body>
  <main class="canvas">
    <section class="card card--front" aria-label="Business card front">
      <div class="tagline-band">Smart copywriting for clever business people</div>
      <h1 class="front-name">Nora Vestrel</h1>
      <div class="portrait" role="img" aria-label="Portrait photograph of Nora Vestrel"></div>
      <ul class="contact-list">
        <li><span class="label">m:</span>0427 593 864</li>
        <li><span class="label">e:</span>nora@noravestrel.com.au</li>
        <li><span class="label">w:</span>noravestrel.com.au</li>
      </ul>
    </section>

    <section class="card card--back" aria-label="Business card back">
      <div class="back-band-top">Smart copywriting</div>
      <div class="brand">
        <span class="brand-mark" aria-hidden="true"></span>
        <span class="brand-name">Nora Vestrel</span>
      </div>
      <div class="back-band-bottom">for clever business people</div>
    </section>
  </main>
</body>
</html>
```